Kindro - Bringing Warmth and Quality to Senior Living

We are a new company based in Sydney, Australia. We have developed a state-of-the-art app for communication between aged care facilities and families.

Kindro has been developed for facilities to augment the best possible care by providing easy, safe and secure communication for families to stay in touch with their loved ones.
Updates

the website needs to be designed so we can add functionality including multilingual support. display in different languages.we also require enquiry and email/data base function. we want it simple and clean so its responsive. the target audience will be 40+ in age. there will be a video on home page. would like to start with 6 pages/ subjects -homepage -about us -our solution -demonstration page, this will be a page that contains videos of people using our product -customer testimonials -contact us

Target Market(s)

Aged care facilities.
Families (over 40’s age group) who are looking for a facility for their loved ones.

Number of Pages Required

5+ page

Font styles to use
Sans Serif

Colors
faa54b
ffffff
0255a3

Requirements
Must have
• - Our corporate colour is #EE8811.
• - If you're using stock photography, please use brimlo prints photos as we have a license for their photos.
• - The design needs to be responsive (mobile and desktop)
• -White space on each page
Nice to have
• -need to leave a place for a future animation video to be added in on the home tab
Should not have
• we don't want flash technology

```html
<!DOCTYPE html>
<html lang="en">
<head>
<meta charset="utf-8">
<title>Kindro - Bringing Warmth and Quality to Senior Living</title>
<link rel="stylesheet" href="https://fonts.googleapis.com/css2?family=Open+Sans:wght@400;600;700&family=Raleway:wght@400;500;600&display=swap">
<style>
:root{
  --orange:#ee8811;
  --orange-soft:#faa54b;
  --blue:#0255a3;
  --icon:#4a9ed6;
  --ink:#222;
  --muted:#777;
  --light:#f4f4f4;
  --card:#eef3f7;
  --form-bg:#e9eef4;
  --footer:#2a3b4a;
  --footer-text:#c5ced6;
  --white:#fff;
}
*{margin:0;padding:0;box-sizing:border-box}
html,body{width:1200px;height:3573px;overflow:hidden}
body{font-family:"Open Sans",Arial,sans-serif;color:var(--ink);background:var(--white);position:relative}
h1,h2,h3{font-family:"Raleway","Open Sans",sans-serif;font-weight:400}
.section{position:absolute;left:0;width:1200px}
.topbar{top:0;height:36px;background:var(--light);font-size:11px;color:#555}
.topbar .intro{position:absolute;left:173px;top:11px}
.topbar-contact{position:absolute;left:462px;top:11px;display:flex;gap:26px}
.topbar-contact span{display:flex;align-items:center;gap:6px}
.topbar .dots{position:absolute;right:173px;top:13px;display:flex;gap:8px}
.topbar .dots i{width:9px;height:9px;border-radius:50%;background:#999;display:block}
.nav{top:36px;height:84px;background:var(--white)}
.brand{position:absolute;left:173px;top:24px;display:flex;align-items:center;gap:10px}
.brand .mark{width:32px;height:32px;border-radius:50%;background:var(--orange)}
.brand .name{font-family:"Raleway",sans-serif;font-size:32px;font-weight:600;color:var(--orange)}
.menu{position:absolute;left:467px;top:34px;display:flex;gap:22px;font-size:12px;font-weight:600;letter-spacing:.3px;color:#333}
.hero{top:120px;height:541px;background:linear-gradient(100deg,#3f4a2c 0%,#56663a 35%,#6f7f48 60%,#8c9a5d 100%)}
.hero .shade{position:absolute;inset:0;background:linear-gradient(90deg,rgba(0,0,0,.35),rgba(0,0,0,0) 60%)}
.hero h1{position:absolute;left:173px;top:206px;width:620px;font-size:29px;line-height:38px;color:var(--white)}
.hero p{position:absolute;left:173px;top:296px;width:460px;font-size:17px;line-height:27px;color:var(--white)}
.badges{position:absolute;left:173px;top:378px;display:flex;gap:12px}
.badges span{width:137px;height:38px;border-radius:7px;background:#111;border:1px solid #555;display:block}
.features{top:661px;height:482px}
.features h2{position:absolute;top:56px;left:0;width:1200px;text-align:center;font-size:22px;line-height:36px;color:#222}
.rule{position:absolute;width:80px;height:1px;background:#ccc;left:560px}
.cards{position:absolute;top:209px;left:173px;display:flex;gap:22px}
.card{width:197px;height:202px;background:var(--card);text-align:center;padding-top:40px}
.card svg{width:56px;height:56px}
.card h3{font-family:"Open Sans",sans-serif;font-size:14px;font-weight:600;margin-top:12px;color:#333}
.card p{font-size:11px;line-height:16px;color:var(--muted);margin:8px auto 0;width:150px}
.about{top:1143px;height:369px;background:linear-gradient(90deg,#f3e6d2 0%,#ecd9bb 40%,#d9ae78 100%)}
.about .photo{position:absolute;right:0;top:0;width:680px;height:369px;background:linear-gradient(90deg,rgba(217,174,120,0) 0%,#c98f55 35%,#8a5b3a 75%,#6b4530 100%)}
.about h2{position:absolute;left:173px;top:72px;font-size:22px;color:#222}
.about .rule{left:173px;top:112px;width:60px;background:#333}
.about .copy{position:absolute;left:173px;top:130px;width:330px;font-size:12px;line-height:19px;color:#333}
.about .copy p+p{margin-top:14px}
.demo{top:1512px;height:745px}
.demo h2{position:absolute;top:68px;width:1200px;text-align:center;font-size:30px;color:#222}
.demo .rule{top:126px;left:550px;width:100px}
.video{position:absolute;background:linear-gradient(135deg,#4b4f55,#6c6f73 50%,#3d4045)}
.video .play{position:absolute;left:50%;top:50%;width:46px;height:46px;margin:-23px 0 0 -23px}
.btn{display:block;background:var(--orange);color:var(--white);font-size:12px;text-align:center;border:0}
.demo .btn{position:absolute;left:538px;top:670px;width:124px;height:39px;line-height:39px}
.enquiry{top:2257px;height:530px;background:var(--form-bg)}
.enquiry .photo{position:absolute;left:0;top:0;width:566px;height:530px;background:linear-gradient(120deg,#f4f2ee 0%,#d6cfc4 35%,#6d4f3c 65%,#3f4f78 100%)}
.enquiry h2{position:absolute;left:610px;top:60px;font-size:26px;color:#222}
.enquiry .sub{position:absolute;left:610px;top:102px;font-size:13px;color:#333}
.enquiry .rule{left:610px;top:135px;width:70px;background:#bbb}
.field{position:absolute;background:var(--white);border:1px solid #d7dde3;font-size:11px;color:#777;padding:11px 10px}
.agree{position:absolute;left:610px;top:384px;width:417px;font-size:10px;line-height:15px;color:#444;display:flex;gap:6px}
.agree i{width:10px;height:10px;border:1px solid #999;background:var(--white);flex:none;margin-top:2px}
.enquiry .btn{position:absolute;left:610px;top:423px;width:417px;height:36px;line-height:36px;font-weight:600}
.testimonial{top:2787px;height:470px}
.testimonial h2{position:absolute;top:64px;width:1200px;text-align:center;font-size:30px;color:#222}
.testimonial .rule{top:122px;left:550px;width:100px}
.testimonial .q{position:absolute;top:174px;width:1200px;text-align:center;font-family:Georgia,serif;font-size:40px;color:#bbb}
.testimonial blockquote{position:absolute;left:240px;top:226px;width:720px;text-align:center;font-size:12px;line-height:22px;color:#555;font-style:italic}
.person{position:absolute;left:528px;top:338px;display:flex;align-items:center;gap:16px}
.person .avatar{width:64px;height:64px;border-radius:50%;background:linear-gradient(135deg,#c99a7a,#8a5f4a)}
.person span{font-size:13px;color:#333}
.footer{top:3257px;height:316px;background:var(--footer);color:var(--footer-text);font-size:11px;line-height:18px}
.footer .brand{top:48px}
.footer .brand .mark{background:transparent;border:2px solid var(--footer-text);width:28px;height:28px}
.footer .brand .name{color:var(--footer-text);font-size:28px}
.footer .about-text{position:absolute;left:173px;top:110px;width:240px}
.footer h3{position:absolute;top:56px;font-family:"Open Sans",sans-serif;font-size:14px;color:var(--white)}
.footer .list{position:absolute;left:476px;top:96px;width:230px}
.footer .list div{display:flex;gap:10px;margin-bottom:12px}
.footer .list svg{flex:none;width:14px;height:14px;margin-top:2px}
.footer .subtext{position:absolute;left:759px;top:96px;width:268px}
.footer .email{position:absolute;left:759px;top:147px;width:268px;height:36px;background:var(--white);color:#666;padding:9px 10px}
.footer .btn{position:absolute;left:759px;top:192px;width:268px;height:36px;line-height:36px;font-weight:600}
.footer .line{position:absolute;left:173px;top:268px;width:854px;height:1px;background:#45566a}
.footer .copy{position:absolute;top:284px;width:1200px;text-align:center;font-size:10px;color:#9aa7b3}
</style>
</head>
<body>

<header class="section topbar">
  <div class="intro">We are a new company based in Sydney, Australia</div>
  <div class="topbar-contact">
    <span><svg width="11" height="9" viewBox="0 0 11 9"><rect x=".5" y=".5" width="10" height="8" fill="none" stroke="#555"/><path d="M.5 .5 5.5 5 10.5 .5" fill="none" stroke="#555"/></svg>info@kindro.com</span>
    <span><svg width="10" height="10" viewBox="0 0 10 10"><path d="M2 1 4 3 3 4.5Q4.5 6.5 5.5 7L7 6 9 8 8 9.5Q3 9 .5 2Z" fill="#555"/></svg>For a free care consultation, call 1 1800 555 012</span>
  </div>
  <div class="dots"><i></i><i></i><i></i><i></i></div>
</header>

<nav class="section nav">
  <div class="brand"><span class="mark"></span><span class="name">Kindro</span></div>
  <div class="menu"><span>HOME</span><span>ABOUT US</span><span>SOLUTION</span><span>DEMONSTRATION</span><span>TESTIMONIAL</span><span>CONTACT US</span></div>
</nav>

<section class="section hero" role="img" aria-label="Photo of a carer walking with an older man in a wheelchair through a leafy park">
  <div class="shade"></div>
  <h1>Aged care facilities. Families who are looking for a facility for their loved ones</h1>
  <p>Imagine being connected to reliable, trustworthy personal Care Providers at your convenience, 24/7</p>
  <div class="badges"><span></span><span></span></div>
</section>

<section class="section features">
  <h2>Everything you need to support you in<br>your efforts as a family aged care</h2>
  <div class="rule" style="top:142px"></div>
  <div class="cards">
    <div class="card">
      <svg viewBox="0 0 56 56" fill="none" stroke="var(--icon)" stroke-width="2"><path d="M8 28 28 10 48 28"/><path d="M14 23V46H42V23"/><rect x="24" y="32" width="8" height="14"/></svg>
      <h3>HOME CARE</h3><p>Sed ut perspiciatis unde omnis iste natus error sit</p>
    </div>
    <div class="card">
      <svg viewBox="0 0 56 56" fill="none" stroke="var(--icon)" stroke-width="2"><path d="M12 40 38 14 44 20 18 46 10 48Z"/><path d="M34 18 40 24M16 38 20 42"/></svg>
      <h3>PERSONAL CARE</h3><p>Sed ut perspiciatis unde omnis iste natus error sit</p>
    </div>
    <div class="card">
      <svg viewBox="0 0 56 56" fill="none" stroke="var(--icon)" stroke-width="2"><path d="M28 46 10 28Q4 20 10 13Q18 6 28 16Q38 6 46 13Q52 20 46 28Z"/><path d="M14 28H22L25 22 30 34 33 28H42"/></svg>
      <h3>MEDICAL CARE</h3><p>Sed ut perspiciatis unde omnis iste natus error sit</p>
    </div>
    <div class="card">
      <svg viewBox="0 0 56 56" fill="none" stroke="var(--icon)" stroke-width="2"><rect x="8" y="17" width="40" height="28" rx="3"/><path d="M21 17V12H35V17M28 24V38M21 31H35"/></svg>
      <h3>CAREGIVER JOBS</h3><p>Sed ut perspiciatis unde omnis iste natus error sit</p>
    </div>
  </div>
</section>

<section class="section about">
  <div class="photo" role="img" aria-label="Photo of a smiling nurse beside an older man in a care home"></div>
  <h2>About Kindro</h2>
  <div class="rule"></div>
  <div class="copy">
    <p>We are a new company based in Sydney, Australia. We have developed a state-of-the-art app for communication between aged care facilities and families</p>
    <p>Kindro has been developed for facilities to augment the best possible care by providing easy, safe and secure communication for families to stay in touch with their loved ones</p>
  </div>
</section>

<section class="section demo">
  <h2>Demonstration</h2>
  <div class="rule"></div>
  <div class="video" style="left:173px;top:197px;width:417px;height:411px" role="img" aria-label="Video still of a carer talking with an older woman">
    <svg class="play" viewBox="0 0 46 46"><circle cx="23" cy="23" r="23" fill="var(--orange)"/><path d="M18 14 33 23 18 32Z" fill="#fff"/></svg>
  </div>
  <div class="video" style="left:610px;top:197px;width:417px;height:196px" role="img" aria-label="Video still of a family visiting an older relative">
    <svg class="play" viewBox="0 0 46 46"><circle cx="23" cy="23" r="23" fill="var(--orange)"/><path d="M18 14 33 23 18 32Z" fill="#fff"/></svg>
  </div>
  <div class="video" style="left:610px;top:412px;width:417px;height:196px" role="img" aria-label="Video still of a carer helping a resident">
    <svg class="play" viewBox="0 0 46 46"><circle cx="23" cy="23" r="23" fill="var(--orange)"/><path d="M18 14 33 23 18 32Z" fill="#fff"/></svg>
  </div>
  <span class="btn">View all</span>
</section>

<section class="section enquiry">
  <div class="photo" role="img" aria-label="Photo of a daughter hugging her elderly mother"></div>
  <h2>Learn more about our Care</h2>
  <div class="sub">Your request will be answered withing 24 hours</div>
  <div class="rule"></div>
  <div class="field" style="left:610px;top:190px;width:200px;height:39px">Name</div>
  <div class="field" style="left:827px;top:190px;width:200px;height:39px">E-mail</div>
  <div class="field" style="left:610px;top:244px;width:417px;height:125px">Message</div>
  <div class="agree"><i></i><span>I agree that my submitted data is being collected and stored. For further details on handling user data</span></div>
  <span class="btn">SEND MESSAGE</span>
</section>

<section class="section testimonial">
  <h2>Testimonial</h2>
  <div class="rule"></div>
  <div class="q">&#8221;</div>
  <blockquote>At vero eos et accusamus et iusto odio dignissimos ducimus qui blanditiis praesentium voluptatum deleniti atque corrupti quos dolores et quas molestias excepturi sint occaecati cupiditate non provident, similique sunt in culpa qui officia deserunt mollitia animi, id est laborum et dolorum fuga</blockquote>
  <div class="person"><span class="avatar" role="img" aria-label="Portrait photo of the reviewer"></span><span>Maren Holt</span></div>
</section>

<footer class="section footer">
  <div class="brand"><span class="mark"></span><span class="name">Kindro</span></div>
  <p class="about-text">Kindro has been developed for facilities to augment the best possible care by providing easy, safe and secure communication for families to stay in touch with their loved ones</p>
  <h3 style="left:476px">Contact Us</h3>
  <div class="list">
    <div><svg viewBox="0 0 14 14"><path d="M7 1A4 4 0 0 0 3 5C3 8 7 13 7 13S11 8 11 5A4 4 0 0 0 7 1Z" fill="var(--orange)"/><circle cx="7" cy="5" r="1.5" fill="var(--footer)"/></svg><span>Sed ut perspiciatis, #2 amnis iste street Nemo enim ipsam voluptatem</span></div>
    <div><svg viewBox="0 0 14 14"><path d="M3 1 6 4 4.5 6Q6.5 8.5 8 9.5L10 8 13 11 11.5 13Q4 12 1 3Z" fill="var(--orange)"/></svg><span>1800 555 012</span></div>
    <div><svg viewBox="0 0 14 14"><rect x="1" y="3" width="12" height="9" fill="var(--orange)"/><path d="M1 3 7 8 13 3" fill="none" stroke="var(--footer)"/></svg><span>info@kindro.com</span></div>
  </div>
  <h3 style="left:759px">Subscribe</h3>
  <p class="subtext">Subscribe to our mailing list to get the updates to your email inbox.</p>
  <div class="email">Email address</div>
  <span class="btn">SUBSCRIBE</span>
  <div class="line"></div>
  <div class="copy">Copyright &#169; 2019, KINDRO. All Rights Reserved</div>
</footer>

</body>
</html>
```